Guarding One's Body Using Sharp Steel Cover

Hi we are producing a self defense course entitled Guarding One's Body Using Sharp Steel: A Complete Manual For Learning The Finest And Handiest Wilderness Tool In Recorded History.

I listed this as a book cover but it will actually be a DVD set, but the book cover model works fine.

See below for design examples - I am thinking we need a cover that will appeal to military/survival type people.

Target Market(s)

survivalists, cops, preppers, gun owners, martial artists, and average people wanting to learn how to defend themselves

Industry/Entity Type

Defense

Requirements
Must have
• Title: GUARDING ONE'S BODY USING SHARP STEEL: A COMPLETE MANUAL FOR LEARNING THE FINEST AND HANDIEST WILDERNESS TOOL IN RECORDED HISTORY
Nice to have
• Please look at these sample designs from other books as a model:
• https://files.plorvexa.org/media/en/4/27/BrindelQXMP.jpg - This stye is ideal.
• Other good examples:
• https://pics2.talvorn.com/8143907_k370.jpg
• http://m.zephquill.com/titles/2719058463k/48071935.jpg
• http://img.crondelmart.com/pics/P/73Tm58QyzFr._BX_KL410_TR316,410_.jpg
• http://3.cdn.wendoplix.net/-RTyZWLMMKAQ/BNWq_hufxaT/BBBBBBBBv8G/DKNp815ZaXW/s1600/Q4710392.JPG

```html
<!DOCTYPE html>
<html lang="en">
<head>
<meta charset="utf-8">
<title>Guarding One's Body Using Sharp Steel — Cover</title>
<link rel="stylesheet" href="https://fonts.googleapis.com/css2?family=Black+Ops+One&family=Roboto:wght@400;700&display=swap">
<style>
  :root {
    --page-bg: #e4e4e2;
    --green-light: #7a9440;
    --green-mid: #5d7a2c;
    --green-dark: #3c561a;
    --ink: #141414;
    --paper: #f4f4f0;
    --steel-dark: #1e1e1e;
    --steel-mid: #3a3a3a;
  }
  html, body {
    margin: 0;
    padding: 0;
    width: 1183px;
    height: 1200px;
    overflow: hidden;
    background: var(--page-bg);
  }
  .canvas {
    position: relative;
    width: 1183px;
    height: 1200px;
  }
  .cover {
    position: absolute;
    left: 201px;
    top: 50px;
    width: 780px;
    height: 1100px;
    box-shadow: 0 6px 24px rgba(0,0,0,0.25);
  }
  .cover svg { display: block; }
  .title-text, .subtitle-text {
    font-family: "Black Ops One", "Impact", sans-serif;
  }
  .format-text {
    font-family: "Roboto", "Arial", sans-serif;
  }
</style>
</head>
<body>
<main class="canvas">
  <section class="cover" aria-label="Guarding One's Body Using Sharp Steel: A Complete Manual For Learning The Finest And Handiest Wilderness Tool In Recorded History">
    <svg width="780" height="1100" viewBox="0 0 780 1100" xmlns="http://www.w3.org/2000/svg">
      <defs>
        <radialGradient id="cover-green" cx="50%" cy="60%" r="75%">
          <stop offset="0%" stop-color="var(--green-light)"/>
          <stop offset="55%" stop-color="var(--green-mid)"/>
          <stop offset="100%" stop-color="var(--green-dark)"/>
        </radialGradient>
        <linearGradient id="knife-tone" x1="0" y1="0" x2="1" y2="0">
          <stop offset="0%" stop-color="var(--steel-mid)"/>
          <stop offset="100%" stop-color="var(--steel-dark)"/>
        </linearGradient>
      </defs>

      <rect class="cover-bg" width="780" height="1100" fill="url(#cover-green)"/>

      <g class="title-block title-text" fill="var(--paper)">
        <text class="title-line title-line--lead" x="40" y="150" font-size="108" textLength="700" lengthAdjust="spacingAndGlyphs">GUARDING ONE'S</text>

        <rect class="title-band" x="40" y="175" width="700" height="175" fill="var(--ink)"/>
        <text class="title-line title-line--key" x="60" y="328" font-size="170" textLength="660" lengthAdjust="spacingAndGlyphs">BODY</text>

        <text class="title-line title-line--link" x="40" y="425" font-size="78" textLength="700" lengthAdjust="spacingAndGlyphs">USING SHARP</text>

        <rect class="title-band" x="40" y="445" width="700" height="225" fill="var(--ink)"/>
        <text class="title-line title-line--hero" x="60" y="640" font-size="205" textLength="660" lengthAdjust="spacingAndGlyphs">STEEL</text>
      </g>

      <g class="knife-visual" role="img" aria-label="Photograph of a black fixed-blade combat knife with serrated edge, lying horizontally">
        <rect x="130" y="705" width="540" height="105" rx="48" fill="url(#knife-tone)"/>
      </g>

      <g class="subtitle subtitle-text" fill="var(--paper)" text-anchor="middle">
        <text x="390" y="885" font-size="38" textLength="680" lengthAdjust="spacingAndGlyphs">A COMPLETE MANUAL FOR LEARNING</text>
        <text x="390" y="935" font-size="38" textLength="560" lengthAdjust="spacingAndGlyphs">THE FINEST AND HANDIEST</text>
        <text x="390" y="985" font-size="38" textLength="700" lengthAdjust="spacingAndGlyphs">WILDERNESS TOOL IN RECORDED HISTORY</text>
      </g>

      <g class="format-mark format-text" fill="var(--paper)">
        <text x="40" y="1055" font-size="22" font-weight="700">DISCA</text>
        <line x1="118" y1="1030" x2="118" y2="1062" stroke="var(--paper)" stroke-width="1.5"/>
        <text x="130" y="1053" font-size="14">32 and 64 Bit</text>
      </g>
    </svg>
  </section>
</main>
</body>
</html>
```